Artisan Food and Beverage company needs label for various product

We are an artisan food and beverage company with a range of different snacks, and beverages, such as chips, cold brew coffee and spreads. Because of this, we have different types of packaging - jars, pouches, bottles.
We are looking for a general label design for our different product ranges. We want to have a design that is adaptable to our different packaging containers but that will also distinguish each product from each other. Eg. Different colors for each product range
Our idea is to have the same general look for all but change the color of the border or sides(?) for each product range, We are thinking of something like this:
1. Border: different color per product range (see the collage pic and the screenshot taken from the Pixel Forge website)
2. Product Category: Eg. Ice Cold Brew , Cheese Dips
- Same size font and type even if one is a pouch and 1 is a flask
3. Product Flavour: Eg. Mocha Latte, Cheddar and Garlic Dip
- Same size font and type even if different packaging (smaler size font
than the product category name
We have added sample pictures of a store label that fits different containers (collage pic) , as well as sample pics of our different packaging containers. We will also have jars for our spreads similar to the jar pic at the top of the collage.
If the design can be editable and the background color (or side color like the one we took a screenshot of here in the website of the crunchy sauce label - pardon that the drop down menu was taken), that is what we have in mind. We should also be able to edit the size so the best pf the whole label so maybe a rectangular label is best.
The "Chef Talbo's" is our official logo.
*Credits to the artist of the Pixel Forge sample labels we took a screenshot of from the website.

```html
<!DOCTYPE html>
<html lang="en">
<head>
<meta charset="utf-8">
<title>Ice Cold Brew – Mocha Latte Labels</title>
<link href="https://fonts.googleapis.com/css2?family=Domine:wght@700&family=Montserrat:wght@500;700&family=Oswald:wght@400;500&display=swap" rel="stylesheet">
<style>
  :root {
    --page: #dcd8d2;
    --cream: #f2eed8;
    --cream-deep: #ebe6c9;
    --brown: #a36c3e;
    --brown-dark: #7d5231;
    --ink: #3f3936;
    --shadow: #d6cfb3;
    --white: #f4efe6;
  }
  html, body {
    margin: 0;
    width: 1200px;
    height: 1200px;
    overflow: hidden;
    background: var(--page);
  }
  .canvas {
    position: relative;
    width: 1200px;
    height: 1200px;
  }

  /* ---------- shared brand mark ---------- */
  .brand {
    position: absolute;
    left: 0; right: 0;
    display: flex;
    align-items: center;
    justify-content: center;
    gap: 8px;
    font-family: "Oswald", sans-serif;
    font-weight: 500;
    color: var(--brown);
    letter-spacing: 1px;
    line-height: 1;
  }
  .brand-dot {
    width: 14px; height: 14px;
    border-radius: 50%;
    background: var(--brown);
  }

  /* ---------- classic badge label ---------- */
  .label-classic {
    position: absolute;
    left: 130px; top: 325px;
    width: 375px; height: 551px;
  }
  .classic-frame { position: absolute; left: 0; top: 0; width: 375px; height: 551px; }
  .label-classic .brand { top: 86px; font-size: 24px; }
  .classic-title {
    position: absolute;
    left: 0; right: 0; top: 205px;
    height: 130px;
    margin: 0;
    text-align: center;
    font-family: "Domine", serif;
    font-weight: 700;
    line-height: 1;
  }
  .classic-title .line-small {
    position: absolute; left: 0; right: 0; top: 0;
    font-size: 41px;
    color: var(--ink);
    text-shadow: 3px 3px 0 var(--shadow);
  }
  .classic-title .line-big {
    position: absolute; left: 0; right: 0; top: 54px;
    font-size: 63px;
    letter-spacing: 3px;
    color: var(--brown);
    text-shadow: 4px 4px 0 var(--shadow);
  }
  .classic-stars {
    position: absolute;
    left: 0; right: 0; top: 352px;
    display: flex; justify-content: center; align-items: center; gap: 10px;
  }
  .classic-star { display: block; }
  .classic-ribbon {
    position: absolute;
    left: 60px; top: 395px;
    width: 255px; height: 50px;
  }
  .classic-flavour {
    position: absolute;
    left: 0; right: 0; top: 397px;
    height: 40px;
    line-height: 40px;
    text-align: center;
    font-family: "Oswald", sans-serif;
    font-weight: 500;
    font-size: 23px;
    letter-spacing: 1px;
    color: var(--white);
  }
  .classic-volume {
    position: absolute;
    left: 0; right: 0; top: 458px;
    text-align: center;
    font-family: "Oswald", sans-serif;
    font-weight: 400;
    font-size: 19px;
    line-height: 1;
    color: var(--ink);
  }

  /* ---------- modern band label ---------- */
  .label-modern {
    position: absolute;
    left: 585px; top: 355px;
    width: 485px; height: 490px;
    background: var(--cream);
    overflow: hidden;
  }
  .modern-texture {
    position: absolute;
    left: 0; top: 0; right: 0; height: 400px;
    background: linear-gradient(180deg, var(--cream) 0%, var(--cream-deep) 100%);
  }
  .label-modern .brand { top: 96px; font-size: 24px; }
  .modern-title {
    position: absolute;
    left: 0; right: 0; top: 162px;
    margin: 0;
    text-align: center;
    font-family: "Montserrat", sans-serif;
    line-height: 1;
  }
  .modern-title .line-small {
    display: block;
    font-weight: 500;
    font-size: 58px;
    color: var(--ink);
    text-shadow: 3px 3px 0 var(--shadow);
  }
  .modern-title .line-big {
    display: block;
    margin-top: 14px;
    font-weight: 700;
    font-size: 86px;
    letter-spacing: 2px;
    color: var(--brown);
    text-shadow: 4px 4px 0 var(--shadow);
  }
  .modern-dots {
    position: absolute;
    left: 0; right: 0; top: 352px;
    display: flex; justify-content: center; align-items: center; gap: 14px;
  }
  .modern-dots span { border-radius: 50%; background: var(--brown); }
  .modern-band {
    position: absolute;
    left: 0; right: 0; bottom: 0; height: 90px;
    background: linear-gradient(90deg, var(--brown-dark), var(--brown) 50%, var(--brown-dark));
    text-align: center;
  }
  .modern-flavour {
    margin-top: 14px;
    font-family: "Oswald", sans-serif;
    font-weight: 500;
    font-size: 29px;
    line-height: 1.2;
    letter-spacing: 1.5px;
    color: var(--white);
  }
  .modern-volume {
    margin-top: 2px;
    font-family: "Oswald", sans-serif;
    font-weight: 400;
    font-size: 16px;
    line-height: 1.2;
    color: var(--white);
  }
</style>
</head>
<body>
<main class="canvas">

  <section class="label-classic">
    <svg class="classic-frame" viewBox="0 0 375 551" width="375" height="551" aria-hidden="true">
      <path fill="var(--cream)" d="M0,56 L52,56 Q68,56 76,40 Q105,0 187.5,0 Q270,0 299,40 Q307,56 323,56 L375,56 L375,495 L323,495 Q307,495 299,511 Q270,551 187.5,551 Q105,551 76,511 Q68,495 52,495 L0,495 Z"/>
      <path fill="none" stroke="var(--brown)" stroke-width="3" d="M19,73 L58,73 Q78,73 88,53 Q112,17 187.5,17 Q263,17 287,53 Q297,73 317,73 L356,73 L356,478 L317,478 Q297,478 287,498 Q263,534 187.5,534 Q112,534 88,498 Q78,478 58,478 L19,478 Z"/>
    </svg>
    <div class="brand"><span class="brand-dot"></span>Chef Talbo's</div>
    <h1 class="classic-title"><span class="line-small">ICE COLD</span><span class="line-big">BREW</span></h1>
    <div class="classic-stars" aria-hidden="true">
      <svg class="classic-star" width="22" height="22" viewBox="0 0 24 24"><path fill="var(--brown)" d="M12 1l3.3 7 7.7.9-5.7 5.2 1.6 7.6L12 17.9 5.1 21.7l1.6-7.6L1 8.9 8.7 8z"/></svg>
      <svg class="classic-star" width="30" height="30" viewBox="0 0 24 24"><path fill="var(--brown)" d="M12 1l3.3 7 7.7.9-5.7 5.2 1.6 7.6L12 17.9 5.1 21.7l1.6-7.6L1 8.9 8.7 8z"/></svg>
      <svg class="classic-star" width="22" height="22" viewBox="0 0 24 24"><path fill="var(--brown)" d="M12 1l3.3 7 7.7.9-5.7 5.2 1.6 7.6L12 17.9 5.1 21.7l1.6-7.6L1 8.9 8.7 8z"/></svg>
    </div>
    <svg class="classic-ribbon" viewBox="0 0 255 50" width="255" height="50" aria-hidden="true">
      <path fill="var(--brown-dark)" d="M0,14 L30,14 L30,50 L0,50 L12,32 Z"/>
      <path fill="var(--brown-dark)" d="M255,14 L225,14 L225,50 L255,50 L243,32 Z"/>
      <rect x="22" y="2" width="211" height="40" fill="var(--brown)"/>
    </svg>
    <div class="classic-flavour">MOCHA LATTE</div>
    <div class="classic-volume">300 ml</div>
  </section>

  <section class="label-modern">
    <div class="modern-texture" role="img" aria-label="Soft wavy line pattern in pale cream tones"></div>
    <div class="brand"><span class="brand-dot"></span>Chef Talbo's</div>
    <h1 class="modern-title"><span class="line-small">ICE COLD</span><span class="line-big">BREW</span></h1>
    <div class="modern-dots" aria-hidden="true">
      <span style="width:4px;height:4px"></span>
      <span style="width:7px;height:7px"></span>
      <span style="width:11px;height:11px"></span>
      <span style="width:17px;height:17px"></span>
      <span style="width:11px;height:11px"></span>
      <span style="width:7px;height:7px"></span>
      <span style="width:4px;height:4px"></span>
    </div>
    <div class="modern-band">
      <div class="modern-flavour">MOCHA LATTE</div>
      <div class="modern-volume">300 ml</div>
    </div>
  </section>

</main>
</body>
</html>
```